Business Card Design Project

Corwen Property Management

Our Business is residential property management, we therefore need a card that displays a professional image, but is clear and concise, and easy to read
Updates

We are committed now guys and girls, loving what we are seeing so far! 

Target Market(s)

Landlords, Rental Property Owners

Industry/Entity Type

Residential

Requirements
Must have
• Dean Fosterly - Principal
Tessa Fosterly - Director (Property Management)

PO Box 718
Holloway SA 5093

Dean: 0419 372 508
Tessa: 0419 613 947

www.corwenpropertymanagement.com.au
admin@corwenpropertymanagement.com.au

Nice to have
• I would like the card to be double sided, white background on the information side and then colour on the reverse, in blue or black and incorporating our logo

```html
<!DOCTYPE html>
<html lang="en">
<head>
<meta charset="utf-8">
<title>Corwen Property Management – Business Card</title>
<link href="https://fonts.googleapis.com/css2?family=Lato:wght@400;700;900&display=swap" rel="stylesheet">
<style>
  :root {
    --page-bg: #e6e9ec;
    --brand-blue: #1f73c2;
    --brand-blue-dark: #1760a6;
    --rule-blue: #3a8ad6;
    --ink: #222222;
    --logo-grey: #5a5a5a;
    --band-black: #242424;
    --paper: #ffffff;
  }
  * { box-sizing: border-box; margin: 0; padding: 0; }
  html, body {
    width: 1200px;
    height: 960px;
    overflow: hidden;
    background: var(--page-bg);
    font-family: "Lato", Arial, sans-serif;
  }
  .canvas {
    width: 1200px;
    height: 960px;
    display: flex;
    flex-direction: column;
    align-items: center;
    justify-content: center;
    gap: 56px;
  }
  .card {
    width: 660px;
    height: 400px;
    position: relative;
    overflow: hidden;
    box-shadow: 0 6px 18px rgba(0,0,0,0.15);
  }

  /* Information side */
  .card-front {
    background: var(--paper);
    border-top: 16px solid var(--brand-blue);
    border-bottom: 26px solid var(--brand-blue);
    display: flex;
    flex-direction: column;
    align-items: center;
    padding-top: 34px;
  }
  .brand {
    display: flex;
    align-items: center;
    gap: 14px;
  }
  .brand-mark {
    width: 44px;
    height: 44px;
    background: var(--brand-blue);
  }
  .brand-name {
    font-weight: 700;
    font-size: 30px;
    color: var(--logo-grey);
    letter-spacing: 0.2px;
  }
  .contacts {
    width: 560px;
    margin-top: 34px;
  }
  .contact-row {
    text-align: center;
    padding: 8px 0 6px;
    border-bottom: 2px solid var(--rule-blue);
    color: var(--ink);
    white-space: nowrap;
  }
  .contact-name {
    font-size: 26px;
    text-transform: uppercase;
  }
  .contact-detail { font-size: 16px; }
  .details {
    margin-top: 16px;
    text-align: center;
    font-size: 17px;
    line-height: 1.4;
    color: var(--ink);
  }
  .details .web {
    color: var(--brand-blue-dark);
    font-weight: 700;
    font-size: 18px;
  }

  /* Colour side */
  .card-back {
    background: var(--brand-blue);
  }
  .card-back .brand {
    position: absolute;
    left: 0; right: 0;
    top: 140px;
    justify-content: center;
    gap: 18px;
  }
  .card-back .brand-mark {
    width: 56px;
    height: 56px;
    background: var(--paper);
  }
  .card-back .brand-name {
    color: var(--paper);
    font-size: 36px;
  }
  .back-band {
    position: absolute;
    left: 0; right: 0; bottom: 0;
    height: 44px;
    background: var(--band-black);
    display: flex;
    align-items: center;
    justify-content: center;
    color: var(--paper);
    font-weight: 700;
    font-size: 17px;
    letter-spacing: 0.6px;
  }
</style>
</head>
<body>
<main class="canvas">
  <section class="card card-front" aria-label="Business card information side">
    <div class="brand">
      <span class="brand-mark"></span>
      <span class="brand-name">Corwen Property Management</span>
    </div>
    <div class="contacts">
      <p class="contact-row">
        <span class="contact-name">Dean Fosterly</span>
        <span class="contact-detail"> | Principal | T: 0419 372 508</span>
      </p>
      <p class="contact-row">
        <span class="contact-name">Tessa Fosterly</span>
        <span class="contact-detail"> | Director (Property Management) | T: 0419 613 947</span>
      </p>
    </div>
    <div class="details">
      <p>E: admin@corwenpropertymanagement.com.au</p>
      <p>PO Box 718, Holloway SA 5093</p>
      <p class="web">www.corwenpropertymanagement.com.au</p>
    </div>
  </section>

  <section class="card card-back" aria-label="Business card colour side">
    <div class="brand">
      <span class="brand-mark"></span>
      <span class="brand-name">Corwen Property Management</span>
    </div>
    <div class="back-band">www.corwenpropertymanagement.com.au</div>
  </section>
</main>
</body>
</html>
```